Wine Importer Needs a Wordpress Template

Our company, Corbusan Wine Merchants Ltd, requires a Wordpress template for our new website location (tarnelcask.ie).

We specialise in importing Moldovan wine into Ireland. I have attached a presentation that has background information about the main winery and its wine. I would very much like to see something similar to this in feel and colour. I have also attached our logo which might be useful.

We are very much open to new ideas, so long as the result is something that is clean and easy to use.

Many thanks.
Updates

Project Deadline Extended
Reason: I have extended the deadline by a few days given that I was unable to respond timely to queries. My apologies to all for this. I will be available from now until the new deadline.

Project Deadline Extended

Industry/Entity Type

It Company

```html
<!DOCTYPE html>
<html lang="en">
<head>
<meta charset="utf-8">
<title>Corbusan Wine Merchants</title>
<link rel="stylesheet" href="https://fonts.googleapis.com/css2?family=Merriweather:ital,wght@0,300;0,400;0,700;1,700&family=Arimo:wght@400;700&family=Courgette&display=swap">
<style>
:root{
  --green:#33b466;
  --green-dark:#27944f;
  --green-deep:#1f7a40;
  --ink:#333;
  --muted:#666;
  --rule:#cfcfcf;
  --nav:#d3ddd9;
  --paper:#fff;
  --panel:#f1f1f1;
  --blue:#2f86c6;
  --charcoal:#2e2e2e;
}
*{box-sizing:border-box;margin:0;padding:0}
html,body{width:1200px;height:2299px;overflow:hidden;background:var(--paper)}
body{font-family:"Merriweather",Georgia,serif;color:var(--ink);position:relative}
.abs{position:absolute}

/* top strip */
.top-strip{left:0;top:0;width:1200px;height:43px;background:var(--green);border-bottom:3px solid var(--green-deep)}
.social-top{left:898px;top:8px;display:flex;gap:10px}
.social-top span{width:25px;height:25px;border-radius:50%;background:#fff;display:block}

/* header */
.header{left:0;top:43px;width:1200px;height:130px}
.account{left:120px;top:33px;font-size:14px;color:#333}
.phone{left:118px;top:68px;font-size:13px;color:#555;display:flex;align-items:center;gap:8px}
.logo-tab{left:470px;top:0;width:260px;height:130px}
.brand{left:480px;top:0;width:240px;height:130px;display:flex;flex-direction:column;align-items:center;justify-content:center;gap:8px}
.brand .mark{width:34px;height:34px;border-radius:50%;background:var(--green-dark)}
.brand .name{font-size:17px;font-weight:700;color:var(--green-dark);text-align:center;line-height:1.35}
.basket-label{left:838px;top:33px;font-size:13px;color:var(--green-dark)}
.checkout{left:980px;top:31px;width:92px;height:20px;background:var(--green-dark);color:#fff;font:700 12px "Arimo",Arial,sans-serif;border-radius:3px;display:flex;align-items:center;justify-content:center}
.basket-box{left:838px;top:57px;width:237px;height:35px;background:#e9e9e9;border:1px solid #d8d8d8;font:13px "Arimo",Arial,sans-serif;color:#555;display:flex;align-items:center;justify-content:center}

/* nav */
.nav{left:0;top:173px;width:1200px;height:46px;background:var(--nav)}
.nav a{position:absolute;top:15px;font-size:12px;color:#333;text-decoration:none;letter-spacing:.3px}
.nav a.home{left:112px;top:8px;width:87px;height:30px;background:#555;border-radius:15px;color:#fff;display:flex;align-items:center;justify-content:center;box-shadow:inset 0 2px 3px #222}

/* hero */
.hero{left:0;top:219px;width:1200px;height:402px;
  background:radial-gradient(ellipse 520px 300px at 880px 210px,#3a2a22 0%,#6b4a34 35%,rgba(160,70,50,0) 75%),
             radial-gradient(ellipse 700px 380px at 330px 200px,#e7c9a6 0%,#b77a57 45%,#6a2f25 100%)}
.hero-cap-title{left:103px;top:121px;height:48px;padding:0 14px;background:var(--green);color:#fff;font-size:27px;font-style:italic;font-weight:700;display:flex;align-items:center;border:2px solid #fff}
.hero-cap-sub{left:103px;top:170px;width:286px;height:48px;padding:0 10px;background:#fff;color:#333;font-size:24px;display:flex;align-items:center}
.dots{left:552px;top:630px;display:flex;gap:6px}
.dots span{width:12px;height:12px;border-radius:50%;background:#d5d5d5}
.dots span.on{background:var(--green-dark)}

/* offer band */
.offer{left:0;top:659px;width:1200px;height:196px;background:var(--green);border-top:3px solid var(--green-deep)}
.ribbon{left:146px;top:-3px;width:108px;height:138px}
.ribbon-text{left:146px;top:22px;width:108px;text-align:center;font:18px/1.3 "Courgette",cursive;color:#fff}
.offer-title{left:291px;top:37px;font-size:29px;color:#fff;font-weight:400}
.offer-copy{left:294px;top:88px;width:595px;font-size:11.5px;line-height:1.62;color:#fff}
.read-more{left:964px;top:83px;width:120px;height:40px;background:var(--blue);border-radius:3px;color:#fff;font:700 13px "Arimo",Arial,sans-serif;display:flex;align-items:center;justify-content:center;border-bottom:2px solid #1f5e8e}

/* section titles */
.rule{height:2px;background:var(--rule)}
.section-title{width:1200px;left:0;text-align:center;font-size:30px;font-weight:300;color:var(--green-dark);letter-spacing:1px}

/* collections */
.coll{text-align:center}
.coll h3{font-size:18px;font-weight:400;color:#333;height:36px;line-height:36px;white-space:nowrap}
.coll .shot{margin:0 auto;height:224px}
.coll.active{width:229px}
.coll.active h3{background:var(--green);color:#fff}
.coll.active .shot{width:229px;background:radial-gradient(ellipse 70% 80% at 60% 55%,#2a2a2a 0%,#494949 45%,#5e5e5e 100%)}
.coll.plain{width:200px}
.coll.plain .shot{width:180px}
.tone-red{background:radial-gradient(ellipse 45% 65% at 55% 60%,#24302a 0%,#5d6d62 35%,#e9ede9 75%,#fff 100%)}
.tone-dark{background:radial-gradient(ellipse 45% 65% at 50% 62%,#1f2a22 0%,#4f6a58 35%,#e8eee9 75%,#fff 100%)}
.arrow{width:55px;height:92px;border:1px solid #d8d8d8;background:#fff}
.view-all{left:0;width:1200px;text-align:center;font-size:13px;letter-spacing:1px;color:#333}

/* sidebar */
.sidebar{left:101px;top:1392px;width:262px;height:544px;border:1px solid #ececec;background:#fafafa}
.sidebar h4{position:absolute;left:12px;top:12px;font-size:24px;font-weight:400;color:var(--green-dark);letter-spacing:.5px}
.sidebar ul{position:absolute;left:12px;top:58px;width:236px;list-style:none}
.sidebar li{height:34px;border-bottom:1px dashed #d6d6d6;font:13px/34px "Arimo",Arial,sans-serif;color:#444;padding-left:22px;position:relative}
.sidebar li::before{content:"»";position:absolute;left:2px;top:0;color:#888;font-size:15px}

/* products */
.prod{width:220px;height:220px}
.prod.boxed{border:1px solid #ccc}
.tone-champagne{background:radial-gradient(ellipse 32% 60% at 50% 55%,#c99a52 0%,#e8cf9c 40%,#fbf6ec 75%,#fff 100%)}
.tone-white{background:radial-gradient(ellipse 45% 62% at 52% 58%,#d9d39a 0%,#eee9c8 40%,#fbfaf2 75%,#fff 100%)}
.tone-sparkling{background:radial-gradient(ellipse 45% 62% at 50% 58%,#2f4a33 0%,#8fa58a 32%,#f0ecd2 62%,#fff 100%)}
.quick{left:0;width:100%;height:34px;display:flex;align-items:center;justify-content:center;color:#fff;font:700 11px "Arimo",Arial,sans-serif;letter-spacing:1px}
.sale{width:24px;height:50px;background:var(--green-dark);clip-path:polygon(0 0,100% 0,100% 100%,50% 78%,0 100%);color:#fff;font:700 6px "Arimo",Arial,sans-serif;text-align:center;padding-top:6px}
.price{width:220px;text-align:center;font:700 12px "Arimo",Arial,sans-serif;color:#222}
.price s{color:#888;font-weight:400;margin-right:4px}
.price b{color:var(--green-dark)}

/* footer */
.footer{left:109px;top:2004px;width:956px;height:211px;background:var(--panel)}
.fcol{position:absolute;top:31px;font-family:"Arimo",Arial,sans-serif}
.fcol h5{font-size:13px;font-weight:700;color:#333;margin-bottom:6px;letter-spacing:.3px}
.fcol li{list-style:none;font-size:10.5px;line-height:15.8px;color:#555}
.fcol.social li{display:flex;align-items:center;gap:8px;line-height:32px;font-size:11px}
.fcol.social li span{width:18px;height:18px;border-radius:3px;background:#3b5a9a;display:block}
.bottom-social{left:123px;top:2238px;display:flex;gap:9px}
.bottom-social span{width:26px;height:26px;border-radius:50%;background:#5e8fc8;display:block}
.copyright{left:0;width:1144px;top:2246px;text-align:center;font:11px "Arimo",Arial,sans-serif;color:#555}
.payments{left:808px;top:2240px;display:flex;gap:7px}
.payments span{width:36px;height:22px;border-radius:3px;background:#d9dde4;display:block}
</style>
</head>
<body>

<div class="abs top-strip">
  <div class="abs social-top" aria-label="Social links"><span></span><span></span><span></span><span></span><span></span></div>
</div>

<header class="abs header">
  <div class="abs account">Login &nbsp;or Create an account</div>
  <div class="abs phone">
    <svg width="14" height="12" viewBox="0 0 14 12"><path d="M1 4c0-2 2-3 6-3s6 1 6 3l-3 1-1-2H5L4 5 1 4zM3 6h8l1 5H2z" fill="#27944f"/></svg>
    020 7000 4821 | Mon-Fri 10am-7pm
  </div>
  <svg class="abs logo-tab" viewBox="0 0 260 130"><path d="M12 130 A118 118 0 0 1 248 130" fill="#fff" stroke="#d4d4d4" stroke-width="2"/></svg>
  <div class="abs brand">
    <span class="mark"></span>
    <span class="name">Corbusan<br>Wine Merchants</span>
  </div>
  <div class="abs basket-label">View Basket</div>
  <div class="abs checkout">Checkout ›</div>
  <div class="abs basket-box">Your basket is currently empty.</div>
</header>

<nav class="abs nav">
  <a class="home" href="#">HOME</a>
  <a href="#" style="left:230px">MENU »</a>
  <a href="#" style="left:343px">BLOG »</a>
  <a href="#" style="left:461px">PAGES »</a>
  <a href="#" style="left:590px">GALLERY »</a>
  <a href="#" style="left:736px">EATURES »</a>
  <a href="#" style="left:898px">CONTACT &amp; RESERVATION</a>
</nav>

<section class="abs hero" role="img" aria-label="Restaurant table with candles and glasses, a row of wine and spirit bottles on the right">
  <div class="abs hero-cap-title">Cabernet Sauvignon Wine</div>
  <div class="abs hero-cap-sub">All Month 30% off</div>
</section>
<div class="abs dots"><span></span><span></span><span></span><span class="on"></span><span></span></div>

<section class="abs offer">
  <svg class="abs ribbon" viewBox="0 0 108 138"><polygon points="0,0 108,0 108,138 54,112 0,138" fill="#2e2e2e" stroke="#1b1b1b" stroke-width="2"/></svg>
  <div class="abs ribbon-text">Special<br>Offer!</div>
  <h2 class="abs offer-title">Special Offer Of The Month</h2>
  <p class="abs offer-copy">Ipsum is simply dummy text of the printing and typesetting industry. Lorem Ipsum has been the industry's standard dummy text ever since the 1500s, when an unknown printer took a galley of type and scrambled it to make a type specimen book. It has survived not only five centuries, but also the leap into electronic typesetting, remaining</p>
  <div class="abs read-more">Read More</div>
</section>

<div class="abs rule" style="left:101px;top:884px;width:997px"></div>
<h2 class="abs section-title" style="top:884px;line-height:48px">FEATURED COLLECTIONS</h2>
<div class="abs rule" style="left:101px;top:930px;width:997px"></div>

<div class="abs arrow" style="left:26px;top:1032px"><svg width="55" height="92"><path d="M31 40l-7 6 7 6" fill="none" stroke="#999" stroke-width="2"/></svg></div>
<div class="abs arrow" style="left:1134px;top:1032px"><svg width="55" height="92"><path d="M24 40l7 6-7 6" fill="none" stroke="#999" stroke-width="2"/></svg></div>

<div class="abs coll active" style="left:107px;top:952px"><h3>Corvella Barolo</h3><div class="shot" role="img" aria-label="Wine glass and bottle under a dark hover overlay"></div></div>
<div class="abs coll plain" style="left:406px;top:952px"><h3>Corvella Barolo</h3><div class="shot tone-red" role="img" aria-label="Red wine glass beside a dark bottle with green capsule"></div></div>
<div class="abs coll plain" style="left:616px;top:952px"><h3>Corvella Barolo</h3><div class="shot tone-dark" role="img" aria-label="Dark green bottle beside a full glass"></div></div>
<div class="abs coll plain" style="left:873px;top:952px"><h3>Corvella Barolo</h3><div class="shot tone-red" role="img" aria-label="Wine glass beside a dark bottle"></div></div>

<div class="abs rule" style="left:101px;top:1238px;width:997px"></div>
<div class="abs view-all" style="top:1248px">VIEW ALL COLLECTIONS</div>
<div class="abs rule" style="left:101px;top:1274px;width:997px"></div>

<h2 class="abs section-title" style="top:1316px">FEATURED WINES</h2>
<div class="abs" style="left:101px;top:1360px;width:997px;height:9px;background:#c6c6c6"></div>

<aside class="abs sidebar">
  <h4>Wine Accessories</h4>
  <ul>
    <li>90+ rated under $20</li><li>Best Wine Deals</li><li>Fine Wine</li><li>Type/Varietal</li>
    <li>Style of Wine</li><li>Region</li><li>Rating Source</li><li>Type/Varietal</li>
    <li>Style of Wine</li><li>Best Wine Deals</li><li>Fine Wine</li><li>Type/Varietal</li>
    <li>Style of Wine</li><li>Best Wine Deals</li>
  </ul>
</aside>

<div class="abs prod boxed tone-champagne" style="left:388px;top:1394px" role="img" aria-label="Champagne bottle with gold label">
  <div class="abs quick" style="top:74px;background:#111">QUICK SHOP</div>
  <div class="abs quick" style="top:108px;background:var(--green-dark)">ADD TO CART</div>
</div>
<div class="abs price" style="left:388px;top:1622px">€530.00</div>

<div class="abs prod tone-white" style="left:630px;top:1394px" role="img" aria-label="White wine glass and bottle"></div>
<div class="abs sale" style="left:826px;top:1392px">SALE</div>
<div class="abs price" style="left:630px;top:1622px"><s>€1,800.00</s><b>€1,670.00</b></div>

<div class="abs prod tone-sparkling" style="left:874px;top:1394px" role="img" aria-label="Sparkling wine bottle and flute"></div>
<div class="abs sale" style="left:1070px;top:1392px">SALE</div>
<div class="abs price" style="left:874px;top:1622px"><s>€850.00</s><b>€800.00</b></div>

<div class="abs prod tone-sparkling" style="left:370px;top:1694px" role="img" aria-label="Sparkling wine bottle and flute"></div>
<div class="abs sale" style="left:566px;top:1692px">SALE</div>
<div class="abs price" style="left:370px;top:1920px"><s>€850.00</s><b>€800.00</b></div>

<div class="abs prod tone-white" style="left:630px;top:1694px" role="img" aria-label="White wine glass and bottle"></div>
<div class="abs sale" style="left:826px;top:1692px">SALE</div>
<div class="abs price" style="left:630px;top:1920px"><s>€1,800.00</s><b>€1,670.00</b></div>

<div class="abs prod tone-sparkling" style="left:874px;top:1694px" role="img" aria-label="Sparkling wine bottle and flute"></div>
<div class="abs sale" style="left:1070px;top:1692px">SALE</div>
<div class="abs price" style="left:874px;top:1920px"><s>€850.00</s><b>€800.00</b></div>

<div class="abs rule" style="left:101px;top:1968px;width:997px"></div>

<footer class="abs footer">
  <div class="fcol" style="left:30px"><h5>SHOPPING WITH US</h5><ul>
    <li>Delivery Information</li><li>Guarantee</li><li>Store Locator</li><li>Wine Advisors</li><li>Wine Plans</li><li>Hartwell's Unlimited</li><li>Contact Us</li><li>Privacy &amp; Cookies</li><li>Terms &amp; Conditions</li></ul></div>
  <div class="fcol" style="left:245px"><h5>OUR WINE RANGE</h5><ul>
    <li>Browse all wine</li><li>Mixed Cases</li><li>Red Wine</li><li>White Wine</li><li>Sparkling Wine</li><li>Rosé Wine</li><li>Fine Wine</li><li>A-Z List</li></ul></div>
  <div class="fcol" style="left:418px"><h5>LATEST OFFERS</h5><ul>
    <li>Mixed Cases</li><li>Red Wine</li><li>White Wine</li><li>Sparkling Wine</li><li>Rosé Wine</li></ul></div>
  <div class="fcol" style="left:581px"><h5>ABOUT US</h5><ul>
    <li>Our History</li><li>Events &amp; Tastings</li><li>Meet the Team</li><li>Our Vineyards</li><li>Our Partnerships</li><li>Wine for Business</li><li>Wine Education</li><li>Careers</li></ul></div>
  <div class="fcol social" style="left:748px"><h5>JOIN THE CONVERSATION</h5><ul>
    <li><span></span>Follow us on Friendbook</li><li><span style="background:#4aa3df"></span>Join us on Chirper</li><li><span style="background:#c0392b"></span>Watch us on ViewTube</li><li><span style="background:#333"></span>Ronan's Diary</li></ul></div>
</footer>

<div class="abs bottom-social"><span></span><span style="background:#e0672a"></span><span style="background:#3b5a9a"></span><span style="background:#9b3b3b"></span></div>
<div class="abs copyright">Copyright © 2012. All Rights Reserved. Corbusan Wine Merchants Ltd.</div>
<div class="abs payments"><span></span><span></span><span></span><span></span><span></span><span></span><span></span></div>

</body>
</html>
```